Bar Wanderlight VIP Card design

Looking for a design for a VIP card forguests wishing to purchase to avoid cover charges, skipping the line and othe advantages.

We used our logo on last years card.I've also attached a few of our previous cards. Looking for something fresh.

We are not apposed to a vertical card either way would be fine We will have to incorporate the fizz mild logo on the card as well.

Industry/Entity Type

Bar Restaurant www.bar-w.example

Font styles to use
Decorative

```html
<!DOCTYPE html>
<html lang="en">
<head>
<meta charset="utf-8">
<title>Bar Wanderlight VIP Card</title>
<link rel="stylesheet" href="https://fonts.googleapis.com/css2?family=Playfair+Display:wght@700;900&family=Montserrat:wght@700;800&display=swap">
<style>
  :root {
    --backdrop: #262d2e;
    --card: #020202;
    --gold-light: #fff6cf;
    --gold: #e8c24a;
    --gold-deep: #a8781c;
    --star: #f6edc4;
    --badge: #bfe2e6;
    --partner: #ffffff;
  }
  html, body {
    margin: 0;
    width: 1200px;
    height: 800px;
    overflow: hidden;
    background: var(--backdrop);
  }
  .stage {
    position: relative;
    width: 1200px;
    height: 800px;
  }
  .vip-card {
    position: absolute;
    left: 110px;
    top: 125px;
    width: 980px;
    height: 550px;
    border-radius: 42px;
    background: var(--card);
    overflow: hidden;
  }
  .ornament {
    position: absolute;
    width: 300px;
    height: 330px;
    border-radius: 50%;
    background: radial-gradient(circle at 50% 50%, rgba(232,194,74,0.55) 0%, rgba(168,120,28,0.35) 45%, rgba(168,120,28,0.08) 70%, rgba(0,0,0,0) 72%);
  }
  .ornament-left { left: -150px; top: 150px; }
  .ornament-right { right: -150px; top: 70px; }
  .vip-mark {
    position: absolute;
    left: 0;
    right: 0;
    top: 120px;
    text-align: center;
  }
  .vip-title {
    margin: 0;
    font-family: "Playfair Display", serif;
    font-weight: 900;
    font-size: 210px;
    line-height: 1;
    letter-spacing: 4px;
    background: linear-gradient(160deg, var(--gold-deep) 0%, var(--gold) 30%, var(--gold-light) 55%, var(--gold) 75%, var(--gold-deep) 100%);
    -webkit-background-clip: text;
    background-clip: text;
    color: transparent;
  }
  .vip-year {
    margin: 6px 0 0;
    display: flex;
    justify-content: center;
    align-items: center;
    gap: 14px;
    font-family: "Montserrat", sans-serif;
    font-weight: 800;
    font-size: 34px;
    color: var(--star);
  }
  .vip-year svg { width: 20px; height: 20px; fill: var(--star); }
  .vip-year .year { margin: 0 10px; }
  .venue-name {
    position: absolute;
    right: 46px;
    top: 36px;
    display: flex;
    align-items: center;
    gap: 12px;
    font-family: "Playfair Display", serif;
    font-weight: 700;
    font-size: 30px;
    color: var(--badge);
  }
  .venue-name .dot {
    width: 22px;
    height: 22px;
    border-radius: 50%;
    background: var(--badge);
  }
  .partner-name {
    position: absolute;
    left: 60px;
    bottom: 44px;
    display: flex;
    align-items: center;
    gap: 10px;
    font-family: "Montserrat", sans-serif;
    font-weight: 800;
    font-size: 30px;
    color: var(--partner);
  }
  .partner-name .square {
    width: 18px;
    height: 18px;
    background: var(--partner);
  }
</style>
</head>
<body>
<main class="stage">
  <section class="vip-card">
    <div class="ornament ornament-left" role="img" aria-label="Gold filigree mandala ornament"></div>
    <div class="ornament ornament-right" role="img" aria-label="Gold filigree mandala ornament"></div>

    <div class="venue-name"><span class="dot"></span>Bar Wanderlight</div>

    <div class="vip-mark">
      <h1 class="vip-title">VIP</h1>
      <p class="vip-year">
        <svg viewBox="0 0 24 24"><path d="M12 2l2.9 6.9 7.1.6-5.4 4.7 1.7 7.3L12 17.8 5.7 21.5l1.7-7.3L2 9.5l7.1-.6z"/></svg>
        <svg viewBox="0 0 24 24"><path d="M12 2l2.9 6.9 7.1.6-5.4 4.7 1.7 7.3L12 17.8 5.7 21.5l1.7-7.3L2 9.5l7.1-.6z"/></svg>
        <svg viewBox="0 0 24 24"><path d="M12 2l2.9 6.9 7.1.6-5.4 4.7 1.7 7.3L12 17.8 5.7 21.5l1.7-7.3L2 9.5l7.1-.6z"/></svg>
        <span class="year">2023</span>
        <svg viewBox="0 0 24 24"><path d="M12 2l2.9 6.9 7.1.6-5.4 4.7 1.7 7.3L12 17.8 5.7 21.5l1.7-7.3L2 9.5l7.1-.6z"/></svg>
        <svg viewBox="0 0 24 24"><path d="M12 2l2.9 6.9 7.1.6-5.4 4.7 1.7 7.3L12 17.8 5.7 21.5l1.7-7.3L2 9.5l7.1-.6z"/></svg>
        <svg viewBox="0 0 24 24"><path d="M12 2l2.9 6.9 7.1.6-5.4 4.7 1.7 7.3L12 17.8 5.7 21.5l1.7-7.3L2 9.5l7.1-.6z"/></svg>
      </p>
    </div>

    <div class="partner-name"><span class="square"></span>fizz mild</div>
  </section>
</main>
</body>
</html>
```